New Webpage for High Class Expert Witness Services Company

We are looking for a minimalist design for a webpage that just has our logo and an entry form offer to connect with one of our Liaisons.
The entry form should just ask for Name, Email, Contact Info and Description of Project.

Company Name is: The Marlow Crest Advisory Services

Number of Pages Required

1 page

```html
<!DOCTYPE html>
<html lang="en">
<head>
<meta charset="UTF-8">
<title>The Marlow Crest Advisory Services — Connect with a Liaison</title>
<link href="https://fonts.googleapis.com/css2?family=Marcellus&family=Outfit:wght@300;400&display=swap" rel="stylesheet">
<style>
  :root {
    --page-bg: #f5f5f5;
    --ink: #111111;
    --field-border: #b9b9b9;
    --field-text: #1a1a1a;
    --button-bg: #121212;
    --button-text: #ffffff;
    --footer-text: #9a9a9a;
  }
  * { margin: 0; padding: 0; box-sizing: border-box; }
  html, body { width: 1200px; height: 732px; overflow: hidden; }
  body { background: var(--page-bg); font-family: "Outfit", sans-serif; color: var(--ink); }
  .page { position: relative; width: 1200px; height: 732px; overflow: hidden; }
  .hero-visual { position: absolute; inset: 0; width: 1200px; height: 732px; }
  .brand {
    position: absolute; left: 93px; top: 38px;
    display: flex; align-items: center; gap: 10px;
    font-family: "Marcellus", serif; font-size: 17px; letter-spacing: 0.06em;
    color: var(--ink); text-transform: uppercase; line-height: 1.15;
  }
  .brand-mark { width: 26px; height: 26px; background: var(--ink); flex: none; }
  .welcome {
    position: absolute; left: 94px; top: 140px;
    font-family: "Marcellus", serif; font-weight: 400; font-size: 58px; letter-spacing: -0.01em;
  }
  .contact-form { position: absolute; left: 95px; top: 233px; width: 468px; }
  .field {
    display: block; width: 468px; height: 54px; margin-bottom: 21px;
    border: 1px solid var(--field-border); background: transparent;
    padding: 0 34px; font-family: "Outfit", sans-serif; font-size: 16px; color: var(--field-text);
  }
  .field::placeholder { color: var(--field-text); opacity: 1; }
  .send-button {
    display: block; width: 467px; height: 65px; margin-top: -1px;
    background: var(--button-bg); color: var(--button-text); border: none;
    font-family: "Outfit", sans-serif; font-size: 18px; cursor: pointer;
  }
  .footer-note {
    position: absolute; left: 84px; top: 688px;
    font-size: 12px; font-weight: 300; color: var(--footer-text);
  }
</style>
</head>
<body>
<main class="page">
  <svg class="hero-visual" viewBox="0 0 1200 732" role="img" aria-label="Photo of a glowing cyan security shield with a fingerprint and padlock icons hovering above a desk in a dark office">
    <defs>
      <radialGradient id="shieldGlow" cx="960" cy="390" r="360" gradientUnits="userSpaceOnUse">
        <stop offset="0" stop-color="#1fc8e8"/>
        <stop offset="0.35" stop-color="#0d6d8c"/>
        <stop offset="0.7" stop-color="#1a2129"/>
        <stop offset="1" stop-color="#0b0d10"/>
      </radialGradient>
    </defs>
    <path d="M826,0 C790,60 735,110 756,160 C780,220 880,260 866,330 C855,400 690,430 648,500 C620,560 700,580 682,640 C670,690 630,710 618,732 L1200,732 L1200,0 Z" fill="url(#shieldGlow)"/>
  </svg>

  <div class="brand"><span class="brand-mark"></span>The Marlow Crest<br>Advisory Services</div>

  <h1 class="welcome">Welcome!</h1>

  <form class="contact-form">
    <input class="field" type="text" placeholder="Name" aria-label="Name">
    <input class="field" type="email" placeholder="Email" aria-label="Email">
    <input class="field" type="tel" placeholder="Phone Number" aria-label="Phone Number">
    <input class="field" type="text" placeholder="Project Description" aria-label="Project Description">
    <button class="send-button" type="submit">Send</button>
  </form>

  <p class="footer-note">© Copyright 2026 | The Marlow Crest Advisory Services | All Right Reserved</p>
</main>
</body>
</html>
```